Website Design Front page Holistic Members site & Natural Therapist Directory

I need a modern, fresh unique look for a natural therapy and holistic/ Spiritual directory & educational website. It needs to be clear, colourful, inviting and suitable for both sexes - young and old. I want it look fresh and super modern.

I will require the design in .psd format and anything in the centre section including rotational image needs to be supplied in .ai so I can break down the components and colours used will also be needed for frames and banners.

Target Market(s)

all ages, male and female. It must appeal to both therapists and general public.

Requirements
Must have
• Logo obviously. Room for a video player 300 x 250. And small introduction text panel. Must follow the layout in file attached. Also a rotating image up the top, in main section (have supplied example image alter as you like - man pointing top right). Have also supplied example of text to have on it. 16 Menu bars on left frame, under home. Must have 6 prominent links to main pages of site. Have included images use if you want or else use your own. These 6 are, Find a Psychic/ Medium, Find a Natural Therapist, Find a Business/ Club/ School, Find an Event/ Workshop, Find a Product, Holistic Career Centre.I have also attached a shot of the emag, although nothing special in design, useful for complimentary colour choices but not limited to. Another link image/ banner would be Free Chat Now.Another if room and not over crowded would be compare memberships. Can use leader board and leader ad board. Also require the footer to be designed and delivered in .ai similar to craft pebble with link image to chatterly and blurbo.
Nice to have
• Compare memberships link would be great but not essential... don't want page to look too busy.
Should not have
• Must not be too busy.. think zen with a modern twist.

```html
<!DOCTYPE html>
<html lang="en">
<head>
<meta charset="utf-8">
<title>Kindred Echo – Share. Learn. Grow.</title>
<link rel="stylesheet" href="https://fonts.googleapis.com/css2?family=Arimo:wght@400;700&family=Roboto+Condensed:wght@300;400&display=swap">
<style>
  :root {
    --brand-blue: #0a5aa6;
    --nav-blue: #0d62b0;
    --footer-blue: #0a4f9c;
    --footer-stripe: #7fb4e8;
    --heading-blue: #1a6bb0;
    --text-grey: #444;
    --dark-grey: #333;
    --green: #7cc832;
    --orange: #f08a10;
    --panel-grey: #f1f1f1;
    --white: #fff;
  }
  * { box-sizing: border-box; margin: 0; padding: 0; }
  html, body { width: 870px; height: 1200px; overflow: hidden; background: var(--white); }
  body { position: relative; font-family: "Arimo", Arial, sans-serif; color: var(--text-grey); }

  .site-header { position: absolute; left: 0; top: 0; width: 870px; height: 115px; background: linear-gradient(#fff, #f4f4f4); border-top: 4px solid #eee; }
  .brand { position: absolute; left: 40px; top: 42px; display: flex; align-items: center; gap: 8px; }
  .brand-dot { width: 26px; height: 26px; border-radius: 50%; background: #c03aa0; }
  .brand-name { font-family: "Arimo", Arial, sans-serif; font-weight: 700; font-size: 22px; color: var(--dark-grey); }
  .leaderboard { position: absolute; left: 332px; top: 15px; width: 510px; height: 85px; border-radius: 3px; background: linear-gradient(90deg, #e7e3ee 0%, #f3eef4 50%, #d9cdbf 80%, #b59a7c 100%); }
  .leaderboard-label { position: absolute; left: 0; top: 20px; width: 258px; text-align: center; font-size: 20px; line-height: 24px; color: #444; }

  .main-nav { position: absolute; left: 0; top: 115px; width: 870px; height: 33px; background: var(--nav-blue); border-top: 1px solid #3f86c8; display: flex; align-items: center; padding-left: 25px; gap: 0; }
  .main-nav a { color: var(--white); font-size: 13px; text-decoration: none; padding: 4px 7px; margin-right: 6px; border-radius: 3px; }
  .main-nav a.is-current { background: var(--white); color: #222; }

  .hero { position: absolute; left: 0; top: 148px; width: 870px; height: 277px; }
  .hero-scene { position: absolute; inset: 0; background: linear-gradient(180deg, #1f7ed0 0%, #4da3e6 45%, #8cc6ef 62%, #2f86c8 70%, #6fb0e0 85%, #e9f3fa 100%); }
  .hero-figure { position: absolute; left: 85px; top: 55px; width: 270px; height: 210px; border-radius: 6px; background: linear-gradient(180deg, #e9eef2, #cfd8df); opacity: .85; }
  .hero-title { position: absolute; left: 408px; top: 67px; font-weight: 700; font-size: 37px; letter-spacing: .5px; color: #f4f8fb; text-shadow: 0 1px 3px rgba(0,0,0,.25); }
  .btn-hero { position: absolute; top: 137px; width: 171px; height: 43px; border-radius: 4px; font-weight: 700; font-size: 20px; display: flex; align-items: center; justify-content: center; gap: 10px; box-shadow: 0 2px 4px rgba(0,0,0,.25); }
  .btn-join { left: 426px; background: linear-gradient(#fff, #e4e4e4); color: #555; }
  .btn-chat { left: 608px; background: linear-gradient(#8fd943, #62b41e); color: var(--white); }

  .content { position: absolute; left: 26px; top: 425px; width: 816px; height: 600px; background: var(--white); box-shadow: 0 0 8px rgba(0,0,0,.12); }
  .welcome-title { position: absolute; left: 29px; top: 35px; font-family: "Roboto Condensed", Arial Narrow, sans-serif; font-weight: 300; font-size: 21px; line-height: 25px; color: var(--dark-grey); }
  .welcome-title span { color: var(--heading-blue); }
  .welcome-text { position: absolute; left: 31px; top: 87px; width: 430px; font-size: 11px; line-height: 14.4px; color: var(--text-grey); }
  .welcome-tagline { position: absolute; left: 31px; top: 187px; font-size: 11px; color: var(--heading-blue); }
  .btn-learn { position: absolute; left: 350px; top: 223px; width: 104px; height: 28px; border-radius: 4px; background: linear-gradient(#f9a02a, #ea7c08); color: var(--white); font-size: 12px; display: flex; align-items: center; justify-content: center; gap: 7px; box-shadow: 0 1px 3px rgba(0,0,0,.2); }

  .video { position: absolute; left: 530px; top: 38px; width: 256px; height: 216px; background: #000; }
  .video-screen { position: absolute; left: 0; top: 0; width: 256px; height: 190px; background: linear-gradient(180deg, #0d1e4a 0%, #3b69b3 45%, #0b1a46 60%, #2d5aa6 80%, #0a1838 100%); }
  .video-title { position: absolute; left: 9px; top: 5px; font-size: 9px; color: var(--white); }
  .video-bar { position: absolute; left: 0; top: 190px; width: 256px; height: 26px; background: linear-gradient(#f6f6f6, #dcdcdc); display: flex; align-items: center; font-size: 9px; color: #333; }
  .video-brand { position: absolute; right: 34px; top: 8px; font-weight: 700; font-size: 9px; color: #444; }

  .divider { position: absolute; left: 10px; top: 289px; width: 580px; height: 1px; background: linear-gradient(90deg, transparent, #ddd 20%, #ddd 80%, transparent); }

  .finder { position: absolute; width: 172px; }
  .finder-title { font-family: "Roboto Condensed", Arial Narrow, sans-serif; font-size: 16px; color: var(--heading-blue); height: 23px; white-space: nowrap; }
  .finder-image { width: 170px; height: 85px; border: 1px solid #ddd; }

  .testimonial { position: absolute; left: 630px; top: 303px; width: 164px; height: 118px; background: var(--panel-grey); border-radius: 4px; padding: 14px 12px 0 16px; font-size: 12.5px; line-height: 15.5px; color: var(--text-grey); }
  .testimonial::after { content: ""; position: absolute; left: 122px; bottom: -16px; border-left: 16px solid var(--panel-grey); border-bottom: 16px solid transparent; }
  .testimonial-name { position: absolute; left: 678px; top: 424px; font-size: 12px; font-style: italic; color: var(--orange); }
  .compare { position: absolute; left: 630px; top: 466px; width: 164px; height: 111px; background: linear-gradient(180deg, #eef0f2, #d5dbe0); border: 1px solid #ddd; }
  .compare-label { position: absolute; left: 0; bottom: 0; width: 100%; height: 47px; background: rgba(20,110,200,.9); color: var(--white); font-weight: 700; font-size: 18px; line-height: 17px; padding: 5px 9px; }

  .site-footer { position: absolute; left: 0; top: 1053px; width: 870px; height: 147px; background: var(--footer-blue); border-top: 4px solid var(--footer-stripe); color: var(--white); }
  .sitemap-title { position: absolute; left: 26px; top: 14px; font-weight: 700; font-size: 11px; }
  .sitemap-col { position: absolute; top: 39px; list-style: none; font-size: 10.5px; line-height: 15.3px; }
  .copyright { position: absolute; right: 28px; top: 14px; font-size: 10.5px; }
  .social { position: absolute; left: 757px; width: 83px; height: 30px; border-radius: 3px; display: flex; align-items: center; justify-content: center; gap: 5px; font-weight: 700; font-size: 14px; color: var(--white); }
  .social-chatterly { top: 44px; background: #3a5a98; }
  .social-blurbo { top: 84px; background: #3ab3e6; }
  .social-dot { width: 8px; height: 8px; border-radius: 50%; background: var(--white); }
</style>
</head>
<body>

<header class="site-header">
  <div class="brand">
    <span class="brand-dot"></span>
    <span class="brand-name">Kindred Echo</span>
  </div>
  <div class="leaderboard" role="img" aria-label="Advertising leaderboard with a soft bokeh background and glass bottles with cork stoppers">
    <div class="leaderboard-label">Leader ad board<br>600 x 100</div>
  </div>
</header>

<nav class="main-nav">
  <a class="is-current" href="#">Home</a>
  <a href="#">Career Centre</a>
  <a href="#">Education Centre</a>
  <a href="#">Therapist Finder</a>
  <a href="#">Psychic Finder</a>
  <a href="#">Business Finder</a>
  <a href="#">Events Calendar</a>
  <a href="#">Social Community</a>
</nav>

<section class="hero">
  <div class="hero-scene" role="img" aria-label="Blue sky over a calm sea"></div>
  <div class="hero-figure" role="img" aria-label="Man in white clothes sitting cross-legged on a cushion, pointing to the upper right"></div>
  <h1 class="hero-title">SHARE. LEARN. GROW.</h1>
  <div class="btn-hero btn-join">Join Now</div>
  <div class="btn-hero btn-chat">Free Chat
    <svg width="36" height="24" viewBox="0 0 36 24"><ellipse cx="14" cy="10" rx="12" ry="8" fill="#fff" stroke="#9aa" stroke-width="1"/><ellipse cx="24" cy="14" rx="10" ry="7" fill="#eef" stroke="#9aa" stroke-width="1"/><path d="M26 20 L31 24 L28 19Z" fill="#eef"/></svg>
  </div>
</section>

<main class="content">
  <h2 class="welcome-title">WELCOME TO <span>KINDRED ECHO COMMUNITY<br>&amp; CHAT ROOMS</span></h2>
  <p class="welcome-text">We hope you will explore the various features our site has to offer. We created this online space for log on and create a dynamic member profile, collaborate on projects, share your ideas and expertise - and, most important, connect with your fellow members. Share, collaborate, exchange and grow - that's why we're here and we hope you are too. Engage and explore anytime, from anywhere there's a web connection.</p>
  <p class="welcome-tagline">Share. Learn. Grow.</p>
  <div class="btn-learn">Learn More
    <svg width="16" height="16" viewBox="0 0 16 16"><circle cx="8" cy="8" r="7" fill="none" stroke="#fff" stroke-width="1.2"/><path d="M6.5 5 L10.5 8 L6.5 11Z" fill="#fff"/></svg>
  </div>

  <div class="video">
    <div class="video-screen" role="img" aria-label="Video still of trees reflected in a still blue lake"></div>
    <span class="video-title">Om Shanti</span>
    <svg style="position:absolute;left:104px;top:79px" width="54" height="36" viewBox="0 0 54 36"><rect x="1" y="1" width="52" height="34" rx="6" fill="rgba(0,0,0,.7)" stroke="#888"/><path d="M20 9 L36 18 L20 27Z" fill="#fff"/></svg>
    <div class="video-bar">
      <svg width="70" height="26" viewBox="0 0 70 26"><path d="M12 8 L20 13 L12 18Z" fill="#333"/><line x1="30" y1="3" x2="30" y2="23" stroke="#bbb"/><path d="M37 10 h3 l4 -4 v14 l-4 -4 h-3z" fill="#555"/><line x1="62" y1="3" x2="62" y2="23" stroke="#bbb"/></svg>
      <span>0:00 / 6:26</span>
    </div>
    <span class="video-brand" style="top:198px">Vidora</span>
    <svg style="position:absolute;right:7px;top:197px" width="14" height="12" viewBox="0 0 14 12"><path d="M1 4V1h3M10 1h3v3M13 8v3h-3M4 11H1V8" fill="none" stroke="#444" stroke-width="1.4"/></svg>
  </div>

  <div class="divider"></div>

  <div class="finder" style="left:21px;top:318px">
    <div class="finder-title">FIND A PSYCHIC</div>
    <div class="finder-image" role="img" aria-label="Candle on an old book beside tarot cards" style="background:linear-gradient(135deg,#2a1d12,#8a6a3a 55%,#e8e2d0 70%,#1a1410)"></div>
  </div>
  <div class="finder" style="left:209px;top:318px">
    <div class="finder-title">FIND A THERAPIST</div>
    <div class="finder-image" role="img" aria-label="Woman receiving a head massage" style="background:linear-gradient(90deg,#bcd8f2,#f1ece6 50%,#bcd8f2)"></div>
  </div>
  <div class="finder" style="left:397px;top:318px">
    <div class="finder-title">FIND A BUSINESS/SCHOOL</div>
    <div class="finder-image" role="img" aria-label="Spa treatment room with massage beds" style="background:linear-gradient(180deg,#8a6a1e,#c9a44a 50%,#e07a20 80%,#6a4a1a)"></div>
  </div>
  <div class="finder" style="left:21px;top:458px">
    <div class="finder-title">FIND AND EVENT</div>
    <div class="finder-image" role="img" aria-label="Hand writing with a pen on a planner" style="background:linear-gradient(135deg,#dfe7f3,#f7f7f7 50%,#c7d4e6)"></div>
  </div>
  <div class="finder" style="left:209px;top:458px">
    <div class="finder-title">FIND A PRODUCT</div>
    <div class="finder-image" role="img" aria-label="Essential oil bottles beside a pink flower" style="background:linear-gradient(90deg,#f2e8ee,#e9c7d6 35%,#c8a06a 65%,#3a2a1e)"></div>
  </div>
  <div class="finder" style="left:397px;top:458px">
    <div class="finder-title">HOLISTIC CAREER CENTRE</div>
    <div class="finder-image" role="img" aria-label="Blue sign reading jobs against a bright sky" style="background:linear-gradient(135deg,#1a3f8a,#3a78c8 50%,#cfe3f6)"></div>
  </div>

  <blockquote class="testimonial">"I read your latest magazine &amp; I have to tell you I thoroughly enjoyed it. I learnt a lot. I can't wait for next months edition!"</blockquote>
  <div class="testimonial-name">Megan, QLD</div>

  <div class="compare" role="img" aria-label="Three smiling people chatting in a bright office">
    <div class="compare-label">Compare<br>Membership</div>
  </div>
</main>

<footer class="site-footer">
  <div class="sitemap-title">Site Map</div>
  <ul class="sitemap-col" style="left:26px">
    <li>Career Centre</li><li>Education Centre</li><li>Therapist Finder</li><li>Psychic Finder</li>
  </ul>
  <ul class="sitemap-col" style="left:133px">
    <li>Business Finder</li><li>Events Calendar</li><li>Social Community</li>
  </ul>
  <div class="copyright">Copyright © 2011 Kindredecho</div>
  <div class="social social-chatterly">chatterly</div>
  <div class="social social-blurbo"><span class="social-dot"></span>blurbo</div>
</footer>

</body>
</html>
```